Dana Wrenfield Photography Business Card

I am looking for a simple, yet elegant business card for my photography business.

It is a short turn around project as the cards need to be printed within 48 hours. So the earlier you submit, the more likely you are to be chosen.

I am a professional portrait, sports and commercial photographer located in Brisbane, Australia. I am looking for a professional business card to distribute to professional clients. The card needs to be professional and easy to read. It must have my contact information as listed below.

Industry/Entity Type

Business

Contact Information for Business Card

Dana Wrenfield Photography
www.danawrenfieldphoto.com.au
dana@danawrenfieldphoto.com.au
+61 437 582 906

Font styles to use
Serif
Sans Serif

Colors
ffc214
fece3e
fee18a

Requirements
Must have
• Must have contact information as above,
• Please use a similar colourscheme to the one provided in the logo upload.
Nice to have
• A very simple, design, happy to have some geometric shapes etc. Must look professional

```html
<!DOCTYPE html>
<html lang="en">
<head>
<meta charset="utf-8">
<title>Dana Wrenfield Photography – Business Card</title>
<link rel="stylesheet" href="https://fonts.googleapis.com/css2?family=Raleway:wght@300&family=Archivo+Black&family=Open+Sans:wght@400&display=swap">
<style>
  :root {
    --backdrop: #ecebe8;
    --card: #f4f4f4;
    --pattern: #e2e2e2;
    --charcoal: #3a3a3c;
    --ink: #111111;
    --text-grey: #555555;
    --gold: #c8901c;
    --yellow: #ffc214;
    --yellow-mid: #fece3e;
  }
  * { box-sizing: border-box; margin: 0; padding: 0; }
  html, body {
    width: 1200px; height: 800px; overflow: hidden;
    background: var(--backdrop);
  }
  .canvas { position: relative; width: 1200px; height: 800px; }

  .card {
    position: absolute; left: 340px; width: 520px; height: 300px;
    border-radius: 12px; overflow: hidden; background: var(--card);
    box-shadow: 0 4px 14px rgba(0,0,0,0.15);
  }
  .card--front { top: 50px; }
  .card--back { top: 430px; }

  /* front */
  .front__top-band { position: absolute; top: 0; left: 0; right: 0; height: 10px; background: var(--charcoal); }
  .front__pattern { position: absolute; top: 10px; left: 0; right: 0; height: 140px;
    background: linear-gradient(180deg, var(--pattern), #ececec); }
  .front__rule { position: absolute; top: 150px; left: 0; right: 0; height: 4px; background: var(--yellow); }
  .front__bottom-band { position: absolute; bottom: 0; left: 0; right: 0; height: 14px;
    background: linear-gradient(180deg, var(--yellow-mid), var(--yellow)); }

  .brand { position: absolute; display: flex; align-items: center; gap: 16px; }
  .brand__dot { width: 72px; height: 72px; border-radius: 50%; background: var(--gold); flex: none; }
  .brand__name {
    font-family: "Raleway", sans-serif; font-weight: 300; color: var(--charcoal);
    text-transform: uppercase; line-height: 1;
  }
  .brand__name span { display: block; }
  .brand--front { top: 42px; left: 95px; }
  .brand--front .brand__name { font-size: 27px; }
  .brand--front .brand__name span + span { font-size: 14px; margin-top: 4px; }

  .front__name { position: absolute; top: 170px; left: 0; right: 0; text-align: center; line-height: 1; }
  .front__name-main { font-family: "Archivo Black", sans-serif; font-size: 22px; color: var(--ink); text-transform: uppercase; }
  .front__name-sub { font-family: "Open Sans", sans-serif; font-size: 14px; color: var(--text-grey); text-transform: uppercase; letter-spacing: 1px; margin-top: 3px; }

  .contact { position: absolute; display: flex; align-items: center; gap: 8px;
    font-family: "Open Sans", sans-serif; font-size: 12.5px; color: var(--text-grey); }
  .contact svg { width: 13px; height: 13px; fill: var(--charcoal); flex: none; }
  .contact--phone { top: 230px; left: 0; right: 0; justify-content: center; }
  .contact--email { top: 262px; left: 18px; }
  .contact--web { top: 262px; right: 22px; }

  /* back */
  .back__pattern { position: absolute; inset: 0; background: linear-gradient(180deg, #e6e6e6, var(--card)); }
  .back__sweeps { position: absolute; inset: 0; width: 520px; height: 300px; }
  .back__sweeps path { fill: var(--charcoal); }
  .brand--back { top: 114px; left: 80px; }
  .brand--back .brand__name { font-size: 32px; }
  .brand--back .brand__name span + span { font-size: 16px; margin-top: 4px; }
</style>
</head>
<body>
<main class="canvas">

  <section class="card card--front">
    <div class="front__top-band"></div>
    <div class="front__pattern" role="img" aria-label="Subtle grey geometric diamond pattern"></div>
    <div class="brand brand--front">
      <div class="brand__dot"></div>
      <p class="brand__name"><span>Dana Wrenfield</span><span>Photography</span></p>
    </div>
    <div class="front__rule"></div>
    <div class="front__name">
      <p class="front__name-main">Dana Wrenfield</p>
      <p class="front__name-sub">Photography</p>
    </div>
    <p class="contact contact--phone">
      <svg viewBox="0 0 24 24" aria-hidden="true"><path d="M6.6 10.8a15.1 15.1 0 0 0 6.6 6.6l2.2-2.2a1 1 0 0 1 1-.25 11.4 11.4 0 0 0 3.6.57 1 1 0 0 1 1 1V20a1 1 0 0 1-1 1A17 17 0 0 1 3 4a1 1 0 0 1 1-1h3.5a1 1 0 0 1 1 1c0 1.25.2 2.45.57 3.57a1 1 0 0 1-.25 1z"/></svg>
      +61 437 582 906
    </p>
    <p class="contact contact--email">
      <svg viewBox="0 0 24 24" aria-hidden="true"><path d="M2 5h20v14H2z M3.5 6.5 12 13l8.5-6.5" fill="none" stroke="#3a3a3c" stroke-width="2"/></svg>
      dana@danawrenfieldphoto.com.au
    </p>
    <p class="contact contact--web">
      <svg viewBox="0 0 24 24" aria-hidden="true"><circle cx="12" cy="12" r="10"/><path d="M2 12h20M12 2c3 3 3 17 0 20M12 2c-3 3-3 17 0 20" fill="none" stroke="#f4f4f4" stroke-width="1.5"/></svg>
      www.danawrenfieldphoto.com.au
    </p>
    <div class="front__bottom-band"></div>
  </section>

  <section class="card card--back">
    <div class="back__pattern" role="img" aria-label="Subtle grey geometric diamond pattern"></div>
    <svg class="back__sweeps" viewBox="0 0 520 300" aria-hidden="true">
      <path d="M90 0 C230 12 380 40 520 120 L520 0 Z"/>
      <path d="M70 300 C200 240 380 215 520 235 L520 300 Z"/>
    </svg>
    <div class="brand brand--back">
      <div class="brand__dot"></div>
      <p class="brand__name"><span>Dana Wrenfield</span><span>Photography</span></p>
    </div>
  </section>

</main>
</body>
</html>
```